Ember needs a new design we have an updated logo and want a high qualitative high end feel

feel and aesthetic should be high qualitative like the packaging in a zelvo or the qualatative weight/feel of an zelvo design. modern, elegant bold.probably just the ember logo on the backone vesion could be blue background white letter ... open to ideas
legal, insurance , medical, finance vantor 300
Information Technology
Serif

```html
<!DOCTYPE html>
<html lang="en">
<head>
<meta charset="utf-8">
<title>Ember business card</title>
<link rel="stylesheet" href="https://fonts.googleapis.com/css2?family=Lora:wght@400;700&display=swap">
<style>
  :root {
    --page-bg: #d9d4cd;
    --card-light: #f3f5f7;
    --card-mid: #dfe5ea;
    --navy: #14283f;
    --brand-blue: #1f4e7a;
    --band-soft: #8fa9c4;
    --band-blue: #17589a;
    --band-deep: #0d3b6c;
    --on-band: #dbe4ee;
  }
  * { margin: 0; padding: 0; box-sizing: border-box; }
  html, body { width: 1200px; height: 970px; overflow: hidden; }
  body {
    background: var(--page-bg);
    font-family: "Lora", Georgia, serif;
    position: relative;
  }
  .card {
    position: absolute;
    left: 80px; top: 190px;
    width: 1040px; height: 590px;
    border-radius: 28px;
    overflow: hidden;
    background: linear-gradient(160deg, var(--card-light) 0%, var(--card-mid) 100%);
    box-shadow: 0 18px 40px rgba(0,0,0,0.18);
  }
  .card-band {
    position: absolute;
    left: 0; right: 0; bottom: 0;
    height: 290px;
    background: linear-gradient(100deg, var(--band-soft) 0%, var(--band-blue) 50%, var(--band-deep) 100%);
  }
  .brand {
    position: absolute; left: 70px; top: 150px;
    display: flex; align-items: center; gap: 18px;
  }
  .brand-name {
    font-size: 92px; font-weight: 700; color: var(--brand-blue); line-height: 1;
  }
  .brand-dot {
    width: 26px; height: 26px; border-radius: 50%; background: var(--brand-blue);
  }
  .holder { position: absolute; right: 48px; top: 86px; text-align: right; }
  .holder-name { font-size: 30px; font-weight: 700; color: var(--navy); letter-spacing: 0.5px; }
  .holder-role { font-size: 26px; color: var(--brand-blue); margin-top: 2px; }
  .address {
    position: absolute; right: 48px; top: 342px; text-align: right;
    font-size: 25px; line-height: 33px; color: var(--on-band);
  }
  .contacts {
    position: absolute; right: 48px; top: 432px; list-style: none;
  }
  .contacts li {
    display: flex; align-items: center; justify-content: flex-end; gap: 14px;
    font-size: 25px; line-height: 38px; color: var(--on-band);
  }
  .contact-icon {
    width: 34px; height: 34px; border-radius: 50%;
    border: 2px solid var(--on-band);
    display: flex; align-items: center; justify-content: center;
  }
</style>
</head>
<body>
  <div class="card">
    <div class="card-band" role="img" aria-label="Decorative blue wave band across the lower card"></div>

    <div class="brand">
      <span class="brand-name">ember</span>
      <span class="brand-dot"></span>
    </div>

    <div class="holder">
      <div class="holder-name">NORA WHITFIELD</div>
      <div class="holder-role">Manager</div>
    </div>

    <div class="address">
      <div>PO BOX 418, Harbour Lane</div>
      <div>7th street Geelong</div>
    </div>

    <ul class="contacts">
      <li>(+6) 4821 307 552
        <span class="contact-icon"><svg width="16" height="18" viewBox="0 0 16 18"><rect x="3" y="1" width="10" height="16" rx="2" fill="none" stroke="#dbe4ee" stroke-width="2"/></svg></span>
      </li>
      <li>hello@emberteam.com
        <span class="contact-icon"><svg width="18" height="14" viewBox="0 0 18 14"><rect x="1" y="1" width="16" height="12" fill="none" stroke="#dbe4ee" stroke-width="2"/><path d="M1 1 L9 8 L17 1" fill="none" stroke="#dbe4ee" stroke-width="2"/></svg></span>
      </li>
      <li>www.emberservices.com
        <span class="contact-icon"><svg width="18" height="18" viewBox="0 0 18 18"><circle cx="9" cy="9" r="7.5" fill="none" stroke="#dbe4ee" stroke-width="1.6"/><ellipse cx="9" cy="9" rx="3.5" ry="7.5" fill="none" stroke="#dbe4ee" stroke-width="1.4"/><path d="M1.5 9 H16.5" stroke="#dbe4ee" stroke-width="1.4"/></svg></span>
      </li>
    </ul>
  </div>
</body>
</html>
```